New Business Cards for MB&LR

We need updated business cards for a staff of 15 engineers, estimators, project managers, and sales people. We have recently begun changes to our website and marketing material to improve our look and branding. We are an established fabricator specializing in pressure vessels, tanks, and structural steel. The owners require us to use the existing logo and old english text design. Also, we prefer dark grey or mostly black cards.
Target Market(s)
Engineers, purchasing agents, estimators, and project managers of; mining companies, refineries, industrial construction professionals
Industry/Entity Type
Business
Contact Information for Business Card
Logo, phone, website, email, etc.
Look and feel

```html
<!DOCTYPE html>
<html lang="en">
<head>
<meta charset="utf-8">
<title>MB&amp;LR Business Card</title>
<link rel="stylesheet" href="https://fonts.googleapis.com/css2?family=Roboto:wght@400;500&family=Roboto+Condensed:wght@700&family=UnifrakturMaguntia&display=swap">
<style>
:root{
  --page:#e6e6e6;
  --card-front:#f3f3f3;
  --ink:#1c1c1c;
  --muted:#9a9a9a;
  --text:#3a3a3a;
  --card-back:#1b1b1b;
  --white:#ffffff;
}
*{margin:0;padding:0;box-sizing:border-box}
html,body{width:1200px;height:960px;overflow:hidden;background:var(--page)}
.canvas{position:relative;width:1200px;height:960px}
.card{position:absolute;width:600px;height:344px;box-shadow:0 2px 4px rgba(0,0,0,.25)}
.card-front{left:315px;top:113px;background:var(--card-front)}
.card-back{left:311px;top:472px;background:var(--card-back)}
.edge-tab{position:absolute;top:70px}
.edge-tab.left{left:0}
.edge-tab.right{right:0}
.brand{position:absolute;left:85px;top:87px;width:190px;height:168px;display:flex;align-items:center;justify-content:center;gap:12px}
.brand-square{width:22px;height:22px;background:var(--ink)}
.brand-name{font-family:"Roboto",sans-serif;font-weight:500;font-size:40px;color:var(--ink);letter-spacing:1px}
.divider{position:absolute;left:308px;top:92px;width:1px;height:166px;background:#c8c8c8}
.contact{position:absolute;left:343px;top:92px;font-family:"Roboto",sans-serif;color:var(--text)}
.person-name{font-family:"Roboto Condensed",sans-serif;font-weight:700;font-size:20px;color:var(--ink);line-height:22px}
.person-title{font-size:14px;color:var(--muted);line-height:18px;margin-top:3px}
.address{font-size:14.5px;line-height:18px;margin-top:10px}
.lines{list-style:none;margin-top:9px}
.lines li{display:flex;align-items:center;gap:9px;font-size:14.5px;line-height:19px}
.lines svg{width:14px;height:14px;fill:var(--ink)}
.back-field{position:absolute;inset:0;background:var(--card-back)}
.tagline{position:absolute;left:0;right:0;top:153px;text-align:center;font-family:"UnifrakturMaguntia",serif;font-size:26px;color:var(--white)}
.stamp{position:absolute;left:0;right:0;top:250px;display:flex;flex-direction:column;align-items:center;font-family:"Roboto",sans-serif;color:var(--white)}
.stamp-badges{display:flex;gap:4px}
.stamp-badges span{width:26px;height:26px;border:1.5px solid var(--white);border-radius:3px}
.stamp-title{font-size:7px;font-weight:500;margin-top:3px}
.stamp-sub{font-size:7px;color:#bbb}
</style>
</head>
<body>
<div class="canvas">
  <section class="card card-front">
    <svg class="edge-tab left" width="24" height="204" viewBox="0 0 24 204">
      <polygon points="0,0 24,16 24,188 0,204" fill="#1c1c1c"/>
    </svg>
    <svg class="edge-tab right" width="24" height="204" viewBox="0 0 24 204">
      <g fill="#1c1c1c">
        <polygon points="24,0 0,16 0,188 24,204 24,198 4,186 4,18 24,6"/>
        <rect x="8" y="12" width="2" height="180"/>
        <rect x="12" y="9" width="2" height="186"/>
        <rect x="16" y="7" width="2" height="190"/>
        <rect x="20" y="5" width="2" height="194"/>
      </g>
    </svg>
    <div class="brand"><span class="brand-square"></span><span class="brand-name">MB&amp;LR</span></div>
    <div class="divider"></div>
    <div class="contact">
      <p class="person-name">DANIEL HARLOW</p>
      <p class="person-title">CEO/FOUNDER</p>
      <p class="address">480 Foundry Row<br>Ironridge Falls 84190</p>
      <ul class="lines">
        <li><svg viewBox="0 0 24 24"><path d="M6.6 10.8a15 15 0 0 0 6.6 6.6l2.2-2.2c.3-.3.7-.4 1-.2 1.1.4 2.3.6 3.6.6.6 0 1 .4 1 1V20c0 .6-.4 1-1 1A17 17 0 0 1 3 4c0-.6.4-1 1-1h3.5c.6 0 1 .4 1 1 0 1.3.2 2.5.6 3.6.1.3 0 .7-.2 1z"/></svg>555.318.2046</li>
        <li><svg viewBox="0 0 24 24"><path d="M6 2h12v5H6zM3 8h18v9h-3v5H6v-5H3zm5 7v5h8v-5z"/></svg>555.318.2047</li>
        <li><svg viewBox="0 0 24 24"><path d="M12 2a10 10 0 1 0 0 20 10 10 0 0 0 0-20zm6.9 6h-3a15 15 0 0 0-1.3-3.9A8 8 0 0 1 18.9 8zM12 4c.8 1.2 1.5 2.5 1.9 4h-3.8c.4-1.5 1.1-2.8 1.9-4zM4.3 14a8 8 0 0 1 0-4h3.4a16 16 0 0 0 0 4zm.8 2h3a15 15 0 0 0 1.3 3.9A8 8 0 0 1 5.1 16zm3-8h-3a8 8 0 0 1 4.3-3.9C8.8 5.3 8.4 6.6 8.1 8zM12 20c-.8-1.2-1.5-2.5-1.9-4h3.8c-.4 1.5-1.1 2.8-1.9 4zm2.3-6H9.7a14 14 0 0 1 0-4h4.6a14 14 0 0 1 0 4zm.3 5.9c.6-1.2 1-2.5 1.3-3.9h3a8 8 0 0 1-4.3 3.9zm1.7-5.9a16 16 0 0 0 0-4h3.4a8 8 0 0 1 0 4z"/></svg>www.mbandlr.com</li>
      </ul>
    </div>
  </section>

  <section class="card card-back">
    <div class="back-field" role="img" aria-label="Faint repeating hexagon emblem pattern on dark grey"></div>
    <p class="tagline">Modern Beam &amp; Large Rolling</p>
    <div class="stamp">
      <div class="stamp-badges" role="img" aria-label="Certification badges"><span></span><span></span><span></span></div>
      <p class="stamp-title">CODE VESSEL STAMP</p>
      <p class="stamp-sub">Authorized Manufacturer</p>
    </div>
  </section>
</div>
</body>
</html>
```